VORALUX SYSTEMS BUSINESS CARD DESIGN

WE WANT COMPLETE NEW DESIGN OF OUR BUSINESS CARD. WE ARE AN INTEGRATION COMPANY, WHERE WE INTEGRATE IOT/SMART SYSTEMS TO HOMES AND CORPORATE CUSTOMERS. WE SUPPLY AND INSTALL AUTOMATION PRODUCTS. THE FINAL DESIGN SHOULD COMMUNICATE TECHNOLOGY. THE CARD DESIGN SHOULD BE VERY IMPACT FULL. LOGO NEEDS TO BE THERE. IT WOULD NICE IF THE DESIGN WAS CLEAN. COLORS IS UP TO DESIGNER TO PLAY WITH, OR CAN STICK TO CORPORATE COLORS (FOLLOW LOGO). I HAVE ADDED FEW REFERENCE PHOTOS TO DRAW INSPIRATION MAYBE. I HAVE ADDED A HEX DESIGN, ITS NOT NECESSARY TO USE THIS DESIGN, ITS UPTO DESIGNER, JUST ADDED IF NEEDED TO PLAY WITH DESIGN.

Target Market(s)

Private end users and corporate clients

Industry/Entity Type

technology, home automation, home theaters, building management systems, IOT

Contact Information for Business Card

It should include Employee name, personal number, office number, email address, both in English and arabic. DETAILS TO INCLUDE :DANIEL MARUVEN, MOBILE 0097150738219,OFFCIE 009714368174, DANIEL@VORALUXSYS.CO

Requirements
Must have
• Should feel like a technology company from design. Details both and in English and arabic (or at least have provision for arabic in design).
Nice to have
• I would like logo on one side, and details on the other side. Logo design side should communicate technology with logo. Other side can be clean just with information or also have some design aspects following from logo side. it would be interesting to see submissions with square design as well (that looks like an app Icon). colors could be of logo, red black grey and white. I have added some designs to draw inspiration from

```html
<!DOCTYPE html>
<html lang="en">
<head>
<meta charset="utf-8">
<title>Voralux Systems – Business Card</title>
<link rel="stylesheet" href="https://fonts.googleapis.com/css2?family=Poppins:wght@400;600;700;800;900&display=swap">
<style>
  :root{
    --page:#031d35;
    --card:#04213f;
    --red:#f7374f;
    --white:#ffffff;
    --ink:#0d2440;
  }
  *{margin:0;padding:0;box-sizing:border-box}
  html,body{width:1050px;height:1200px;overflow:hidden;background:var(--page);font-family:"Poppins",sans-serif}
  .canvas{position:relative;width:1050px;height:1200px}
  .card{position:absolute;left:105px;width:840px;height:480px;background:var(--card);border-radius:26px;overflow:hidden;box-shadow:0 10px 24px rgba(0,0,0,.35)}
  .card--front{top:81px}
  .card--back{top:639px}

  /* front */
  .front__tab{position:absolute;left:335px;top:0;width:170px;height:31px;background:var(--white)}
  .front__mark{position:absolute;left:335px;top:84px;width:170px;height:170px;background:var(--white)}
  .front__name{position:absolute;left:0;right:0;top:270px;text-align:center;color:var(--white);font-weight:800;font-size:41px;line-height:48px;letter-spacing:-1px}
  .front__band{position:absolute;left:0;right:0;bottom:0;height:75px;background:var(--red)}
  .front__rule{position:absolute;top:35px;height:4px;background:var(--white)}
  .front__rule--left{left:0;width:297px}
  .front__rule--right{right:0;width:297px}
  .front__url{position:absolute;left:0;right:0;top:20px;text-align:center;color:var(--white);font-weight:700;font-size:19px;letter-spacing:2px}

  /* back */
  .back__mark{position:absolute;left:32px;top:31px;width:102px;height:103px;background:var(--white);display:flex;align-items:center;justify-content:center;text-align:center;color:var(--ink);font-weight:800;font-size:14px;line-height:17px}
  .back__namepanel{position:absolute;left:0;top:176px;width:407px;height:127px;background:var(--white)}
  .back__accent{position:absolute;left:31px;top:31px;width:3px;height:58px;background:var(--red)}
  .back__person{position:absolute;left:52px;top:30px;color:var(--red);font-weight:800;font-size:29px;letter-spacing:-1px;line-height:36px}
  .back__role{position:absolute;left:52px;top:66px;color:var(--ink);font-weight:400;font-size:24px;letter-spacing:.6px;line-height:30px}
  .back__divider{position:absolute;left:431px;top:75px;width:2px;height:338px;background:var(--white)}
  .contact{position:absolute;left:457px;display:flex;align-items:flex-start}
  .contact__icon{width:39px;height:39px;border-radius:50%;background:var(--white);display:flex;align-items:center;justify-content:center;flex:none}
  .contact__text{margin-left:8px;color:var(--white)}
  .contact__label{font-size:14px;font-weight:400;line-height:16px}
  .contact__value{font-size:16px;font-weight:700;letter-spacing:1.6px;line-height:19.5px}
</style>
</head>
<body>
<div class="canvas">

  <section class="card card--front">
    <div class="front__tab"></div>
    <div class="front__mark"></div>
    <h1 class="front__name">VORALUX<br>SYSTEMS</h1>
    <div class="front__band">
      <span class="front__rule front__rule--left"></span>
      <span class="front__rule front__rule--right"></span>
      <p class="front__url">www.company.com</p>
    </div>
  </section>

  <section class="card card--back">
    <div class="back__mark">VORALUX<br>SYSTEMS</div>
    <div class="back__namepanel">
      <span class="back__accent"></span>
      <h2 class="back__person">DANIEL MARUVEN</h2>
      <p class="back__role">General Manager</p>
    </div>
    <span class="back__divider"></span>

    <div class="contact" style="top:74px">
      <span class="contact__icon"><svg width="20" height="22" viewBox="0 0 20 22"><path d="M10 1a7 7 0 0 0-7 7c0 5 7 13 7 13s7-8 7-13a7 7 0 0 0-7-7z" fill="var(--red)"/><circle cx="10" cy="8" r="3" fill="#fff"/></svg></span>
      <div class="contact__text">
        <p class="contact__label">Visit Us here</p>
        <p class="contact__value">Dubai, UAE #210 Qasr Noor<br>Building, Al Wasl<br>Post Box 48215</p>
      </div>
    </div>

    <div class="contact" style="top:163px">
      <span class="contact__icon"><svg width="26" height="26" viewBox="0 0 26 26" fill="none" stroke="var(--red)" stroke-width="1.3"><circle cx="13" cy="13" r="11"/><ellipse cx="13" cy="13" rx="5" ry="11"/><path d="M2 13h22M4 7h18M4 19h18M13 2v22"/></svg></span>
      <div class="contact__text">
        <p class="contact__label">Visit Our Website</p>
        <p class="contact__value">www.voraluxsys.co/</p>
      </div>
    </div>

    <div class="contact" style="top:233px">
      <span class="contact__icon"><svg width="22" height="16" viewBox="0 0 22 16" fill="none" stroke="var(--red)" stroke-width="1.4"><rect x="1" y="1" width="20" height="14" rx="2"/><path d="M1.5 2l9.5 7 9.5-7"/></svg></span>
      <div class="contact__text">
        <p class="contact__label">Email Address</p>
        <p class="contact__value">daniel@voraluxsys.co</p>
      </div>
    </div>

    <div class="contact" style="top:303px">
      <span class="contact__icon"><svg width="20" height="20" viewBox="0 0 24 24"><path d="M6.6 10.8a15 15 0 0 0 6.6 6.6l2.2-2.2a1 1 0 0 1 1-.25 11.4 11.4 0 0 0 3.6.57 1 1 0 0 1 1 1V20a1 1 0 0 1-1 1A17 17 0 0 1 3 4a1 1 0 0 1 1-1h3.5a1 1 0 0 1 1 1c0 1.25.2 2.45.57 3.57a1 1 0 0 1-.25 1z" fill="var(--red)"/></svg></span>
      <div class="contact__text">
        <p class="contact__label">Office Number</p>
        <p class="contact__value">+009714368174</p>
      </div>
    </div>

    <div class="contact" style="top:373px">
      <span class="contact__icon"><svg width="20" height="20" viewBox="0 0 24 24"><path d="M6.6 10.8a15 15 0 0 0 6.6 6.6l2.2-2.2a1 1 0 0 1 1-.25 11.4 11.4 0 0 0 3.6.57 1 1 0 0 1 1 1V20a1 1 0 0 1-1 1A17 17 0 0 1 3 4a1 1 0 0 1 1-1h3.5a1 1 0 0 1 1 1c0 1.25.2 2.45.57 3.57a1 1 0 0 1-.25 1z" fill="var(--red)"/></svg></span>
      <div class="contact__text">
        <p class="contact__label">Mobile Number</p>
        <p class="contact__value">+0097150738219</p>
      </div>
    </div>
  </section>

</div>
</body>
</html>
```